STI/STD Medical Clinic- Wellspring Crest Partners, Inc Website

We are a STI clinic in florida looking for a website. We want to be professional but also playful. We want a buildout similar to the website listed below as our clinic is very similar to theirs.

This is a great example of a clinic doing similar stuff as us. We obviously do not want their color scheme but their format and buildout work. Please see our logo attached for color schemes etc.

https://bluefernclinicmiami.org

Industry/Entity Type

Medical

Coding

Coded - Design and coding required

Number of Pages Required

5+ page

Font styles to use
Sans Serif

```html
<!DOCTYPE html>
<html lang="en">
<head>
<meta charset="utf-8">
<title>Wellspring Crest Partners, Inc</title>
<link href="https://fonts.googleapis.com/css2?family=Jost:wght@400;500;600&display=swap" rel="stylesheet">
<style>
:root{
  --blue:#1a82ec;
  --purple:#5b33d6;
  --violet:#7a2fe0;
  --pink:#e33fd4;
  --orange:#ff6a3d;
  --ink:#1d1d24;
  --body:#3a3a44;
  --muted:#f0f1f3;
  --footer:#17171d;
  --white:#ffffff;
}
*{box-sizing:border-box;margin:0;padding:0}
html,body{width:1200px;height:3555px;overflow:hidden}
body{position:relative;background:var(--white);font-family:'Jost',sans-serif;color:var(--ink)}
.abs{position:absolute}
.center{text-align:center}
.btn{position:absolute;display:flex;align-items:center;justify-content:center;border-radius:16px;color:var(--white);font-size:11.5px;font-weight:500;height:30px}
.btn-violet{background:linear-gradient(90deg,#5b33d6,#b93fe6)}
.btn-blue{background:linear-gradient(90deg,#1a82ec,#4d4af0)}
.btn-coral{background:linear-gradient(90deg,#f1447a,#ff6a3d)}

/* header */
.site-header{position:absolute;left:0;top:0;width:1200px;height:94px;background:var(--white)}
.brand{position:absolute;left:200px;top:26px;display:flex;align-items:center;gap:10px}
.brand-dot{width:34px;height:34px;border-radius:50%;background:var(--violet)}
.brand-name{font-size:19px;font-weight:600;color:var(--violet);line-height:1}
.phone{position:absolute;left:664px;top:26px;font-size:12px;font-weight:500;display:flex;align-items:center;gap:5px}
.nav{position:absolute;top:66px;font-size:10px;font-weight:500;transform:translateX(-50%)}
.nav.active{color:var(--blue)}

/* hero */
.hero-bg{position:absolute;left:0;top:94px;width:1200px;height:1006px;background:var(--muted)}
.hero-art{position:absolute;left:0;top:94px}
.hero-label{left:200px;top:198px;font-size:14px;font-weight:500;color:var(--white);letter-spacing:.4px}
.hero-title{left:200px;top:222px;font-size:36px;font-weight:500;color:var(--white);line-height:44px}
.dots{position:absolute;display:flex;gap:11px}
.dots span{width:10px;height:10px;border-radius:50%;border:1.5px solid var(--white)}
.dots span.on{background:var(--white);box-shadow:inset 0 0 0 2px #777}

/* welcome */
.welcome-art{left:200px;top:662px;width:386px;height:393px;border-radius:50%;background:radial-gradient(circle at 40% 40%,#f2c9f0,#c7c9f6 55%,rgba(240,241,243,0) 72%)}
.welcome-kicker{left:612px;top:686px;font-size:14.5px;font-weight:500;color:var(--blue)}
.welcome-title{left:612px;top:708px;width:385px;font-size:29.5px;font-weight:500;line-height:36px}
.welcome-text{left:612px;width:390px;font-size:10.6px;line-height:15px;color:var(--body)}
.color-bars{position:absolute;top:1099px;left:0;width:1200px;height:5px;display:flex;gap:12px}
.color-bars span{flex:1}

/* sections */
.section-title{left:0;width:1200px;font-size:29px;font-weight:500}
.section-sub{left:0;width:1200px;font-size:10.6px;line-height:15px;color:var(--body)}
.service{position:absolute;width:170px;text-align:center}
.service-icon{width:68px;height:68px;border-radius:50%;margin:0 auto;display:flex;align-items:center;justify-content:center}
.service h3{font-size:12.5px;font-weight:500;margin-top:22px}
.service p{font-size:10.2px;line-height:14px;margin-top:8px;color:var(--body)}
.service a{display:block;font-size:9.5px;font-weight:600;color:var(--blue);margin-top:9px;text-decoration:none;letter-spacing:.3px}

/* team */
.team-band{left:0;top:1747px;width:1200px;height:519px;background:linear-gradient(90deg,#0d8cf0,#4648ec 55%,#6a2fe0)}
.team-card{position:absolute;top:1900px;width:225px;height:225px;color:var(--white);text-align:center}
.team-card .name{position:absolute;left:0;width:100%;top:164px;font-size:14.5px}
.team-card .role{position:absolute;left:0;width:100%;top:184px;font-size:9.5px}
.team-dot{position:absolute;top:2114px;width:22px;height:22px;border-radius:50%;background:var(--white);border:2px solid var(--pink)}

/* partners */
.partner{position:absolute;top:2402px;width:149px;height:80px;background:var(--white);box-shadow:0 2px 10px rgba(0,0,0,.08);display:flex;align-items:center;justify-content:center}
.dots.dark span{border-color:var(--blue)}
.dots.dark span.on{background:var(--blue);box-shadow:inset 0 0 0 2px #fff}

/* booking */
.booking-art{position:absolute;left:0;top:2580px}
.booking-title{left:0;width:1200px;top:2700px;font-size:29px;font-weight:500;line-height:37px;color:var(--white)}
.field{position:absolute;background:var(--white);border-radius:15px;font-size:9.5px;color:#7a7a85;padding:9px 16px}
.booking-note{color:var(--white);font-size:10px}
.check{display:inline-block;width:8px;height:8px;border:1px solid var(--white);margin-right:10px;vertical-align:-1px}

/* footer */
.footer-bg{position:absolute;left:0;top:3190px;width:1200px;height:365px;background:var(--footer)}
.footer-brand{left:200px;top:3270px;width:160px;display:flex;align-items:center;gap:10px}
.footer-h{font-size:14px;font-weight:500;color:var(--white);letter-spacing:.6px}
.footer-link{font-size:10.5px;color:var(--white)}
.store{position:absolute;top:3428px;height:33px;border:1px solid var(--white);border-radius:5px;background:#000;color:var(--white);display:flex;align-items:center;gap:6px;padding:0 10px;font-size:12px}
.store i{width:14px;height:14px;border-radius:3px;background:var(--white);display:block}
.social{position:absolute;top:3430px;width:29px;height:29px;border-radius:50%}
.copyright{left:0;width:1200px;top:3512px;font-size:9.5px;color:var(--white)}
</style>
</head>
<body>

<header class="site-header">
  <div class="brand"><span class="brand-dot"></span><span class="brand-name">Wellspring Crest</span></div>
  <div class="phone">
    <svg width="12" height="12" viewBox="0 0 24 24"><path d="M6 2l4 4-2 3c1 3 4 6 7 7l3-2 4 4-3 4C10 21 3 14 2 5z" fill="none" stroke="#1a82ec" stroke-width="2"/></svg>
    +123-456-7890
  </div>
  <div class="btn btn-blue" style="left:786px;top:19px;width:112px;height:31px">Patient Portal</div>
  <div class="btn btn-coral" style="left:912px;top:19px;width:87px;height:31px">Donate</div>
  <span class="nav active" style="left:470px">HOME</span>
  <span class="nav" style="left:548px">ABOUT US</span>
  <span class="nav" style="left:650px">MEET THE TEAM</span>
  <span class="nav" style="left:750px">SERVICES</span>
  <span class="nav" style="left:826px">NEWS</span>
  <span class="nav" style="left:886px">FAQS</span>
  <span class="nav" style="left:967px">CONTACT US</span>
</header>

<div class="hero-bg"></div>
<svg class="hero-art" width="1200" height="540" viewBox="0 0 1200 540">
  <defs>
    <linearGradient id="heroPhoto" x1="0" y1="0" x2="1" y2="1">
      <stop offset="0" stop-color="#2f5f5a"/><stop offset=".6" stop-color="#5b8a84"/><stop offset="1" stop-color="#97b5b0"/>
    </linearGradient>
    <linearGradient id="heroArc" x1="0" x2="1">
      <stop offset="0" stop-color="#7a2fe0"/><stop offset=".5" stop-color="#9b30e0"/><stop offset="1" stop-color="#7a2fe0"/>
    </linearGradient>
  </defs>
  <path role="img" aria-label="Photo of a stethoscope resting on a medical chart" d="M0 0H1200V250Q600 778 0 250Z" fill="url(#heroPhoto)"/>
  <path d="M276 441Q738 661 1200 254" fill="none" stroke="url(#heroArc)" stroke-width="9"/>
</svg>
<div class="abs hero-label">WELLSPRING CREST PARTNERS</div>
<div class="abs hero-title">Lorem Ipsum is simply dummy<br>text of the printingting</div>
<div class="btn btn-violet" style="left:200px;top:333px;width:163px">Make an Appointment</div>
<div class="btn btn-blue" style="left:378px;top:333px;width:99px">Services</div>
<div class="dots" style="left:563px;top:533px"><span></span><span class="on"></span><span></span><span></span></div>

<div class="abs welcome-art" role="img" aria-label="Colourful interlaced ribbon decoration"></div>
<div class="abs welcome-kicker">Welcome to Wellspring Crest Partners</div>
<div class="abs welcome-title">Lorem Ipsum is simply<br>dummy text of the printing<br>and typesetting</div>
<p class="abs welcome-text" style="top:827px">It is a long established fact that a reader will be distracted by the readable content of a page when looking at its layout. The point of using Lorem Ipsum is that it has a more-or-less normal distribution of letters, as opposed to using 'Content here, content here', making it look like readable English. Many desktop publishing packages and web page editors now use Lorem Ipsum as their default model text, and a search for 'lorem ipsum' will uncover.</p>
<p class="abs welcome-text" style="top:932px">There are many variations of passages of Lorem Ipsum available, but the majority have suffered alteration in some form, by injected humour, or randomised words which don't look even slightly ...</p>
<div class="btn btn-violet" style="left:612px;top:999px;width:100px">About Us</div>

<div class="color-bars"><span style="background:var(--blue)"></span><span style="background:var(--purple)"></span><span style="background:var(--pink)"></span><span style="background:var(--orange)"></span></div>

<h2 class="abs center section-title" style="top:1156px">Our Services</h2>
<p class="abs center section-sub" style="top:1196px">It is a long established fact that a reader will be distracted by the readable content of a page when looking at its layout.<br>The point of using Lorem Ipsum is that it has a more-or-less normal distribution</p>

<div class="service" style="left:205px;top:1253px">
  <div class="service-icon" style="background:var(--blue)"><svg width="28" height="28" viewBox="0 0 24 24" fill="none" stroke="#fff" stroke-width="1.6"><rect x="5" y="4" width="14" height="17" rx="1"/><path d="M9 3h6v3H9zM8 10h8M8 13h8M8 16h8"/></svg></div>
  <h3>PrEP</h3><p>Lorem ipsum dolor sit amet, consectetur adipiscing elit, sed do eiusmod tempor ...</p><a>READ MORE</a>
</div>
<div class="service" style="left:412px;top:1253px">
  <div class="service-icon" style="background:var(--purple)"><svg width="30" height="30" viewBox="0 0 24 24" fill="none" stroke="#fff" stroke-width="1.6"><rect x="3" y="5" width="7" height="14" rx="3.5"/><path d="M3 12h7"/><circle cx="16.5" cy="14" r="4"/><path d="M13.7 11.2l5.6 5.6"/></svg></div>
  <h3>PeP</h3><p>Lorem ipsum dolor sit amet, consectetur adipiscing elit, sed do eiusmod tempor ...</p><a style="color:var(--orange)">READ MORE</a>
</div>
<div class="service" style="left:618px;top:1253px">
  <div class="service-icon" style="background:linear-gradient(135deg,#ff7a3d,#ef3b4f)"><svg width="28" height="28" viewBox="0 0 24 24" fill="none" stroke="#fff" stroke-width="1.6"><path d="M8 4a2 2 0 014 0v10a4 4 0 11-4 0z"/><circle cx="16" cy="5" r="1.6"/></svg></div>
  <h3>Hepatitis C</h3><p>Lorem ipsum dolor sit amet, consectetur adipiscing elit, sed do eiusmod tempor ...</p><a>READ MORE</a>
</div>
<div class="service" style="left:824px;top:1253px">
  <div class="service-icon" style="background:linear-gradient(135deg,#f04fd0,#c63ee0)"><svg width="28" height="28" viewBox="0 0 24 24" fill="none" stroke="#fff" stroke-width="1.6"><path d="M12 3c3 0 4 3 2 6l-6 11M12 3c-3 0-4 3-2 6l6 11"/></svg></div>
  <h3>HIV</h3><p>Lorem ipsum dolor sit amet, consectetur adipiscing elit, sed do eiusmod tempor ...</p><a>READ MORE</a>
</div>

<div class="service" style="left:205px;top:1453px">
  <div class="service-icon" style="background:linear-gradient(135deg,#f04fd0,#c63ee0)"><svg width="28" height="28" viewBox="0 0 24 24" fill="none" stroke="#fff" stroke-width="1.6"><path d="M5 3v6a4 4 0 008 0V3M9 13v3a4 4 0 008 0v-2"/><circle cx="17" cy="12" r="2"/></svg></div>
  <h3>STI</h3><p>Lorem ipsum dolor sit amet, consectetur adipiscing elit, sed do eiusmod tempor ...</p><a>READ MORE</a>
</div>
<div class="service" style="left:412px;top:1453px">
  <div class="service-icon" style="background:linear-gradient(135deg,#ff7a3d,#ef3b4f)"><svg width="28" height="28" viewBox="0 0 24 24" fill="none" stroke="#fff" stroke-width="1.6"><path d="M4 15v-3a8 8 0 0116 0v3"/><rect x="3" y="14" width="4" height="6" rx="1"/><rect x="17" y="14" width="4" height="6" rx="1"/></svg></div>
  <h3>Case Management</h3><p>Lorem ipsum dolor sit amet, consectetur adipiscing elit, sed do eiusmod tempor ...</p><a>READ MORE</a>
</div>
<div class="service" style="left:618px;top:1453px">
  <div class="service-icon" style="background:var(--purple)"><svg width="28" height="28" viewBox="0 0 24 24" fill="none" stroke="#fff" stroke-width="1.6"><rect x="7" y="3" width="10" height="18" rx="2"/><path d="M11 18h2"/></svg></div>
  <h3>Telehealth</h3><p>Lorem ipsum dolor sit amet, consectetur adipiscing elit, sed do eiusmod tempor ...</p><a>READ MORE</a>
</div>
<div class="service" style="left:824px;top:1453px">
  <div class="service-icon" style="background:var(--blue)"><svg width="30" height="30" viewBox="0 0 24 24" fill="none" stroke="#fff" stroke-width="1.6"><path d="M3 4h12v8H8l-3 3v-3H3z"/><path d="M17 8h4v8h-2v3l-3-3h-6v-2"/></svg></div>
  <h3>Language Interpretation</h3><p>Lorem ipsum dolor sit amet, consectetur adipiscing elit, sed do eiusmod tempor ...</p><a>READ MORE</a>
</div>
<div class="btn btn-violet" style="left:519px;top:1654px;width:163px">Make an Appointment</div>

<section class="abs team-band"></section>
<h2 class="abs center section-title" style="top:1801px;color:var(--white)">Meet The Team</h2>
<p class="abs center section-sub" style="top:1841px;color:var(--white)">It is a long established fact that a reader will be distracted by the readable content of a page when looking at its layout.<br>The point of using Lorem Ipsum is that it has a more-or-less normal distribution</p>
<svg class="abs" style="left:188px;top:2004px" width="12" height="18" viewBox="0 0 12 18"><path d="M10 2L3 9l7 7" fill="none" stroke="#fff" stroke-width="2.4"/></svg>
<svg class="abs" style="left:998px;top:2004px" width="12" height="18" viewBox="0 0 12 18"><path d="M2 2l7 7-7 7" fill="none" stroke="#fff" stroke-width="2.4"/></svg>
<div class="team-card" style="left:237px;background:linear-gradient(160deg,#d98be6,#b06ee6)" role="img" aria-label="Portrait photo of a doctor with a stethoscope">
  <div class="name">Standard Chunk</div><div class="role">Lorem Ipsum simply dummy</div>
</div>
<div class="team-card" style="left:488px;background:linear-gradient(160deg,#6a6f80,#b7bac4)" role="img" aria-label="Portrait photo of a doctor in a white coat">
  <div class="name">Finibus Bonorum</div><div class="role">Lorem Ipsum simply dummy</div>
</div>
<div class="team-card" style="left:738px;background:linear-gradient(160deg,#4e5563,#a4a9b4)" role="img" aria-label="Portrait photo of a doctor with glasses">
  <div class="name">Rowan Ashcombe</div><div class="role">Lorem Ipsum simply dummy</div>
</div>
<span class="team-dot" style="left:321px"></span><span class="team-dot" style="left:354px"></span>
<div class="btn btn-coral" style="left:550px;top:2172px;width:100px">View All</div>

<h2 class="abs center section-title" style="top:2320px">Our Partners</h2>
<p class="abs center section-sub" style="top:2359px">It is a long established fact that a reader will be distracted by the readable content .</p>
<div class="partner" style="left:200px"><span style="width:60px;height:40px;background:#2b2b2b;border-radius:4px;display:block"></span></div>
<div class="partner" style="left:363px"><span style="width:50px;height:50px;background:#2f6fd6;border-radius:50%;display:block"></span></div>
<div class="partner" style="left:525px"><span style="width:60px;height:40px;background:#7a4fe0;border-radius:20px;display:block"></span></div>
<div class="partner" style="left:688px"><span style="width:44px;height:44px;background:#ef5a3a;display:block"></span></div>
<div class="partner" style="left:850px"><span style="width:44px;height:44px;background:#2aa86b;border-radius:50%;display:block"></span></div>
<div class="dots dark" style="left:563px;top:2515px"><span></span><span class="on"></span><span></span><span></span></div>

<svg class="booking-art" width="1200" height="640" viewBox="0 0 1200 640">
  <defs>
    <linearGradient id="bookingFill" x1="0" y1="0" x2="1" y2=".3">
      <stop offset="0" stop-color="#6a2fe6"/><stop offset=".55" stop-color="#a03be8"/><stop offset="1" stop-color="#f04ad6"/>
    </linearGradient>
    <linearGradient id="bookingEdge" x1="0" x2="1">
      <stop offset="0" stop-color="#8a3ce6"/><stop offset=".5" stop-color="#f05494"/><stop offset="1" stop-color="#ff6a3d"/>
    </linearGradient>
  </defs>
  <path d="M0 300Q600 -170 1200 300V640H0Z" fill="url(#bookingFill)"/>
  <path d="M0 290Q600 -190 1200 240" fill="none" stroke="url(#bookingEdge)" stroke-width="9"/>
</svg>
<h2 class="abs center booking-title">Now Booking for TeleHealth and<br>In-Person Appointments</h2>
<div class="abs" style="left:294px;top:2800px;width:160px;height:1px;background:rgba(255,255,255,.7)"></div>
<div class="abs" style="left:745px;top:2800px;width:160px;height:1px;background:rgba(255,255,255,.7)"></div>
<div class="abs center booking-note" style="left:0;width:1200px;top:2792px;font-size:11.5px;font-weight:500">Fill out the form to make an appointment</div>
<div class="field" style="left:294px;top:2835px;width:196px;height:30px">Your Name</div>
<div class="field" style="left:502px;top:2835px;width:196px;height:30px">Email</div>
<div class="field" style="left:709px;top:2835px;width:196px;height:30px">Phone</div>
<div class="field" style="left:294px;top:2878px;width:611px;height:80px;border-radius:10px">What are you inquiring about?</div>
<div class="field" style="left:294px;top:2975px;width:611px;height:29px">What is your location preference?</div>
<div class="abs booking-note" style="left:310px;top:3020px;font-size:12px;font-weight:500">What is your appointment preference?</div>
<div class="abs booking-note" style="left:312px;top:3046px"><span class="check"></span>In-Person <span style="display:inline-block;width:28px"></span><span class="check"></span>Telehealth</div>
<div class="abs booking-note" style="left:310px;top:3071px;font-size:9.5px">All in-person appointments require adherence to current Regional Health Council guidelines for COVID-19.</div>
<div class="btn btn-coral" style="left:550px;top:3110px;width:100px">Submit</div>

<div class="footer-bg"></div>
<svg class="abs" style="left:0;top:3140px" width="1200" height="70" viewBox="0 0 1200 70">
  <defs><linearGradient id="footerWave" x1="0" x2="1"><stop offset="0" stop-color="#c03ee8"/><stop offset=".5" stop-color="#f04a9a"/><stop offset="1" stop-color="#ff6a3d"/></linearGradient></defs>
  <path d="M0 66Q300 20 600 50T1200 50V70H0Z" fill="url(#footerWave)"/>
  <path d="M0 72Q300 28 600 58T1200 58V70H0Z" fill="#17171d"/>
</svg>
<div class="abs footer-brand"><span class="brand-dot" style="width:40px;height:40px;flex:none"></span><span class="brand-name" style="color:var(--white);font-size:18px;line-height:22px">Wellspring Crest</span></div>

<div class="abs footer-h" style="left:405px;top:3272px">QUICK LINKS</div>
<div class="abs" style="left:405px;top:3304px;display:flex;flex-direction:column;gap:9.5px">
  <span class="footer-link">Home</span><span class="footer-link">About Us</span><span class="footer-link">Meet The Team</span><span class="footer-link">Services</span><span class="footer-link">News</span><span class="footer-link">FAQs</span><span class="footer-link">Contact Us</span>
</div>

<div class="abs footer-h" style="left:545px;top:3272px">CONTACT US</div>
<div class="abs footer-link" style="left:545px;top:3304px;font-size:12px;display:flex;gap:8px;align-items:center"><svg width="13" height="13" viewBox="0 0 24 24"><path d="M6 2l4 4-2 3c1 3 4 6 7 7l3-2 4 4-3 4C10 21 3 14 2 5z" fill="none" stroke="#1a82ec" stroke-width="2"/></svg>123-456-7890</div>
<div class="abs footer-link" style="left:545px;top:3328px;display:flex;gap:8px;align-items:center"><svg width="13" height="11" viewBox="0 0 24 18"><rect x="1" y="1" width="22" height="16" fill="none" stroke="#1a82ec" stroke-width="2"/><path d="M1 1l11 9 11-9" fill="none" stroke="#1a82ec" stroke-width="2"/></svg>info@wellspringcrest.com</div>
<div class="abs footer-link" style="left:545px;top:3351px;font-size:9.5px;line-height:15px;display:flex;gap:10px"><svg width="10" height="13" viewBox="0 0 16 22"><path d="M8 21s7-8 7-13A7 7 0 001 8c0 5 7 13 7 13z" fill="none" stroke="#1a82ec" stroke-width="2"/></svg><span>Lorem Yard, London, United Kingdom,<br>Ipsum Work - 1234</span></div>
<div class="abs" style="left:545px;top:3395px;font-size:12.5px;font-weight:500;color:var(--blue)">Follow Us</div>
<span class="social" style="left:546px;background:var(--blue)"></span>
<span class="social" style="left:584px;background:var(--pink)"></span>
<span class="social" style="left:622px;background:var(--purple)"></span>
<span class="social" style="left:660px;background:#2f6fe6"></span>

<div class="abs footer-h" style="left:763px;top:3272px">CLINIC LOCATIONS</div>
<div class="abs" style="left:763px;top:3304px;display:flex;flex-direction:column;gap:9.5px">
  <span class="footer-link">Lakemont</span><span class="footer-link">Brindle Bay</span><span class="footer-link">Cedarhollow</span>
</div>
<div class="abs" style="left:763px;top:3392px;font-size:12.5px;font-weight:500;color:var(--blue)">Download Our App</div>
<div class="store" style="left:762px;width:102px"><i></i>PlayNest</div>
<div class="store" style="left:877px;width:102px"><i></i>AppHarbor</div>

<div class="abs" style="left:200px;top:3485px;width:800px;height:1px;background:rgba(255,255,255,.18)"></div>
<p class="abs center copyright">© 2022 <span style="color:var(--blue)">Wellspring Crest Partners</span>. All Right Reserved &nbsp;&nbsp;&nbsp; | &nbsp;&nbsp;&nbsp; Terms and Conditions &nbsp;&nbsp;&nbsp; | &nbsp;&nbsp;&nbsp; Privacy Policy</p>
<svg class="abs" style="left:1092px;top:3506px" width="16" height="18" viewBox="0 0 16 18"><path d="M8 0L16 18L8 13L0 18Z" fill="#7a4fe0"/></svg>

</body>
</html>
```